KFR T Coaching Website

We need a website to post videos, blogs and other information or links.
We teach Jujitsu , combatives, Metaphysical Coaching. I want to tach online and in person. Silver Harbor Institute Deals in several areas of Personal Protection and Coaching.
Training (Martial Arts / combative)
Emotional Intelligence
Leadership Development
Motivation
Our Log is attached.
Similar Websites to what we do ( we want to stand out better).
https://renwoskel.com/
https://bavomure.com/
https://crestlinevigorcoaching.com/
Training , Martial Arts, coaching
2 page

```html
<!DOCTYPE html>
<html lang="en">
<head>
<meta charset="utf-8">
<title>Silver Harbor Institute</title>
<link href="https://fonts.googleapis.com/css2?family=Cinzel:wght@600;700&family=Montserrat:wght@400;500;600;700&display=swap" rel="stylesheet">
<style>
:root{
  --red:#e4262c;
  --ink:#141414;
  --dark:#1d1e21;
  --darker:#141517;
  --white:#ffffff;
  --muted:#5c5c5c;
  --light:#f3f3f3;
}
*{box-sizing:border-box;margin:0;padding:0}
html,body{width:1200px;height:5208px;overflow:hidden}
body{position:relative;font-family:"Montserrat",Arial,sans-serif;background:var(--white);color:var(--ink)}
.abs{position:absolute}
.heading{font-family:"Cinzel",Georgia,serif;font-weight:700;letter-spacing:3px}
.photo{position:absolute}

/* hero */
.hero{position:absolute;left:0;top:0;width:1200px;height:725px;overflow:hidden}
.hero-photo{inset:0;background:linear-gradient(100deg,#2c3a40 0%,#55666b 40%,#b8b2a8 62%,#7f7a74 80%,#3a3a3c 100%)}
.hero-shade{position:absolute;inset:0;background:linear-gradient(90deg,rgba(10,10,12,.55),rgba(10,10,12,.1) 70%),linear-gradient(180deg,rgba(10,10,12,.85) 0,rgba(10,10,12,.4) 190px,rgba(10,10,12,0) 300px)}
.topline{left:72px;top:54px;color:var(--red);font-size:17px;font-weight:600;letter-spacing:1px;display:flex;align-items:center;gap:10px}
.search{left:920px;top:52px;width:210px;height:26px;border-bottom:2px solid var(--white);display:flex;justify-content:flex-end}
.nav{left:0;top:130px;width:1200px;height:30px}
.nav a{position:absolute;color:var(--white);text-decoration:none;font-size:15px;font-weight:600;letter-spacing:1px;text-transform:uppercase}
.nav a.active{color:var(--red)}
.brand-top{left:450px;top:22px;width:300px;text-align:center;color:var(--white)}
.brand-top .mark{width:58px;height:58px;border-radius:50%;border:3px solid var(--white);margin:0 auto 10px}
.brand-top .name{font-family:"Montserrat",Arial,sans-serif;font-weight:700;font-size:20px;letter-spacing:2px}
.hero-title{left:95px;top:298px;color:var(--white);font-size:52px;line-height:62px}
.btn{display:flex;align-items:center;gap:12px;background:var(--red);color:var(--white);border-radius:30px;font-weight:700;font-size:16px;letter-spacing:1px;text-transform:uppercase}
.btn .ico{width:40px;height:40px;border-radius:50%;background:rgba(255,255,255,.2);display:flex;align-items:center;justify-content:center}
.hero .btn{left:100px;top:425px;height:56px;padding:0 26px 0 8px}

/* about */
.about{position:absolute;left:0;top:725px;width:1200px;height:715px;background:var(--dark);overflow:hidden}
.about-photo{inset:0;background:radial-gradient(ellipse at 70% 70%,#3d4b5d 0,#262a31 55%,#1d1e21 100%);opacity:.9}
.about-mark{left:120px;top:130px;width:500px;height:460px;display:flex;flex-direction:column;align-items:center;justify-content:center;gap:28px}
.about-mark .square{width:180px;height:180px;border:8px solid var(--white)}
.about-mark .name{color:var(--white);font-weight:700;font-size:34px;letter-spacing:3px;text-align:center;line-height:44px}
.about h2{left:690px;top:165px;color:var(--white);font-size:44px}
.about p{left:690px;top:240px;width:450px;color:#e6e6e6;font-size:15px;line-height:23px}
.about .btn{left:690px;top:510px;height:48px;padding:0 22px 0 6px;font-size:14px}
.about .btn .ico{width:36px;height:36px}
.edge-bottom{left:0;bottom:0;width:1200px;height:60px;background:var(--white);clip-path:polygon(0 60%,15% 40%,32% 70%,50% 35%,68% 65%,85% 40%,100% 55%,100% 100%,0 100%)}

/* services */
.section-title{position:absolute;left:0;width:1200px;text-align:center;font-size:44px}
.svc{position:absolute;width:460px;height:425px;overflow:hidden}
.svc .label{position:absolute;left:0;bottom:0;width:100%;height:90px;background:linear-gradient(180deg,rgba(0,0,0,0),rgba(0,0,0,.8));color:var(--white);font-family:"Cinzel",Georgia,serif;font-weight:700;font-size:18px;letter-spacing:1.5px;display:flex;align-items:flex-end;padding:0 24px 24px;white-space:nowrap}
.svc.right .label{justify-content:flex-end}
.play{position:absolute;width:90px;height:90px;border-radius:50%;background:rgba(255,255,255,.92);display:flex;align-items:center;justify-content:center}
.center-badge{left:465px;top:2101px;width:270px;height:270px;border-radius:50%;background:var(--white);display:flex;align-items:center;justify-content:center}
.center-badge .inner{width:222px;height:222px;border-radius:50%;background:var(--ink);color:var(--white);font-weight:700;font-size:20px;letter-spacing:2px;text-align:center;line-height:28px;display:flex;align-items:center;justify-content:center}

/* teach */
.teach{position:absolute;left:0;top:2880px;width:1200px;height:860px;background:var(--darker)}
.edge-top{left:0;top:-40px;width:1200px;height:60px;background:var(--darker);clip-path:polygon(0 45%,12% 60%,30% 30%,48% 58%,66% 32%,82% 60%,100% 40%,100% 100%,0 100%)}
.teach .section-title{top:160px;color:var(--white)}
.tcard{position:absolute;top:265px;width:310px;height:400px;background:var(--white)}
.tcard .photo{left:0;top:0;width:310px;height:235px}
.tcard h3{position:absolute;top:258px;width:100%;text-align:center;font-size:26px;letter-spacing:2px}
.tcard p{position:absolute;top:305px;left:30px;width:250px;text-align:center;font-size:13px;line-height:19px;color:var(--muted)}

/* blog */
.bcard{position:absolute;background:var(--white);box-shadow:0 6px 22px rgba(0,0,0,.16)}
.bcard h4{position:absolute;font-weight:700;text-transform:uppercase;font-size:15px;line-height:22px}
.bcard p{position:absolute;font-size:12px;line-height:18px;color:var(--muted)}
.date{position:absolute;display:flex;align-items:center;gap:10px;font-size:13px;color:var(--muted)}

/* footer */
.footer{position:absolute;left:0;top:4650px;width:1200px;height:558px;background:#1b1b1c;color:var(--white)}
.footer .edge-top{background:#1b1b1c}
.f-brand{left:110px;top:125px;width:200px;text-align:center}
.f-brand .mark{width:60px;height:60px;border-radius:50%;border:3px solid var(--white);margin:0 auto 14px}
.f-brand .name{font-weight:700;font-size:20px;letter-spacing:2px;line-height:28px}
.f-social{left:190px;top:330px;width:40px;height:40px;border-radius:50%;background:var(--white)}
.f-col h5{font-family:"Cinzel",Georgia,serif;font-weight:700;font-size:26px;letter-spacing:2px;margin-bottom:26px}
.f-col li{list-style:none;font-size:15px;line-height:31px;color:#e2e2e2}
.contact-row{display:flex;align-items:flex-start;gap:14px;font-size:14px;line-height:20px;margin-bottom:22px;color:#e2e2e2}
.contact-row .ic{width:34px;height:34px;border-radius:50%;background:var(--white);flex:none;display:flex;align-items:center;justify-content:center}
.field{width:240px;height:46px;border:1px solid #bdbdbd;border-radius:4px;font-size:14px;color:#cfcfcf;display:flex;align-items:center;padding-left:16px}
.submit{margin-top:18px;width:130px;height:42px;border-radius:22px;background:var(--red);display:flex;align-items:center;justify-content:center;gap:8px;font-weight:700;font-size:14px;letter-spacing:1px}
.copy{left:0;top:508px;width:1200px;text-align:center;font-size:12px;letter-spacing:1px;color:#cfcfcf}
</style>
</head>
<body>

<header class="hero">
  <div class="photo hero-photo" role="img" aria-label="Students in martial arts uniforms kneeling in a row in a training hall"></div>
  <div class="hero-shade"></div>
  <div class="abs topline">
    <svg width="18" height="18" viewBox="0 0 24 24"><path fill="#e4262c" d="M6.6 10.8a15 15 0 0 0 6.6 6.6l2.2-2.2c.3-.3.7-.4 1-.2 1.1.4 2.3.6 3.6.6.6 0 1 .4 1 1V20c0 .6-.4 1-1 1A17 17 0 0 1 3 4c0-.6.4-1 1-1h3.5c.6 0 1 .4 1 1 0 1.3.2 2.5.6 3.6.1.3 0 .7-.2 1z"/></svg>
    CALL US: 555 019 4820
  </div>
  <div class="abs search">
    <svg width="20" height="20" viewBox="0 0 24 24"><circle cx="10" cy="10" r="6.5" fill="none" stroke="#fff" stroke-width="2.4"/><path d="M15 15l6 6" stroke="#fff" stroke-width="2.4"/></svg>
  </div>
  <div class="abs brand-top">
    <div class="mark"></div>
    <div class="name">SILVER HARBOR INSTITUTE</div>
  </div>
  <nav class="abs nav">
    <a class="active" style="left:75px">Home</a>
    <a style="left:190px">About Us</a>
    <a style="left:338px">Coaching</a>
    <a style="left:765px">Course</a>
    <a style="left:895px">What We Do</a>
    <a style="left:1055px">Contact</a>
  </nav>
  <h1 class="abs heading hero-title">SILVER HARBOR<br>INSTITUTE</h1>
  <a class="abs btn"><span class="ico"><svg width="18" height="18" viewBox="0 0 24 24"><path fill="#fff" d="M6.6 10.8a15 15 0 0 0 6.6 6.6l2.2-2.2c.3-.3.7-.4 1-.2 1.1.4 2.3.6 3.6.6.6 0 1 .4 1 1V20c0 .6-.4 1-1 1A17 17 0 0 1 3 4c0-.6.4-1 1-1h3.5c.6 0 1 .4 1 1 0 1.3.2 2.5.6 3.6.1.3 0 .7-.2 1z"/></svg></span>Get in Touch</a>
</header>

<section class="about">
  <div class="photo about-photo" role="img" aria-label="Dim view of a martial arts mat during practice"></div>
  <div class="abs about-mark">
    <div class="square"></div>
    <div class="name">SILVER HARBOR<br>INSTITUTE</div>
  </div>
  <h2 class="abs heading">ABOUT US</h2>
  <p class="abs">Lorem ipsum dolor sit amet, consectetur adipiscing elit, sed do eiusmod tempor incididunt ut labore et dolore magna aliqua. Ut enim ad minim veniam, quis nostrud exercitation ullamco laboris nisi ut aliquip ex ea commodo consequat. Duis aute irure dolor in reprehenderit in voluptate velit esse cillum dolore eu fugiat nulla pariatur. Excepteur sint occaecat cupidatat non proident, sunt in culpa qui officia deserunt mollit anim id est laborum. Sed ut perspiciatis unde omnis iste natus error sit voluptatem accusantium doloremque laudantium, totam rem aperiam.</p>
  <a class="abs btn"><span class="ico"><svg width="16" height="16" viewBox="0 0 24 24"><path fill="#fff" d="M6.6 10.8a15 15 0 0 0 6.6 6.6l2.2-2.2c.3-.3.7-.4 1-.2 1.1.4 2.3.6 3.6.6.6 0 1 .4 1 1V20c0 .6-.4 1-1 1A17 17 0 0 1 3 4c0-.6.4-1 1-1h3.5c.6 0 1 .4 1 1 0 1.3.2 2.5.6 3.6.1.3 0 .7-.2 1z"/></svg></span>Learn More</a>
  <div class="abs edge-bottom"></div>
</section>

<section class="services">
  <h2 class="section-title heading" style="top:1665px">OUR SERVICES</h2>
  <div class="svc" style="left:100px;top:1782px">
    <div class="photo" style="inset:0;background:linear-gradient(135deg,#6b6d70,#2e2f33 60%,#8a8780)" role="img" aria-label="Two men sparring in a training gym"></div>
    <div class="play" style="left:185px;top:150px"><svg width="34" height="34" viewBox="0 0 24 24"><path d="M7 4l14 8-14 8z" fill="#141414"/></svg></div>
    <div class="label">TRAINING</div>
  </div>
  <div class="svc right" style="left:640px;top:1782px">
    <div class="photo" style="inset:0;background:linear-gradient(135deg,#d8d2c8,#a89c8c 55%,#c7763f)" role="img" aria-label="Counsellor talking with a client across a desk"></div>
    <div class="label">EMOTIONAL INTELLIGENCE</div>
  </div>
  <div class="svc" style="left:100px;top:2265px">
    <div class="photo" style="inset:0;background:linear-gradient(135deg,#7b5a45,#b59c85 50%,#4a4a4e)" role="img" aria-label="Team of colleagues in a meeting room"></div>
    <div class="label">LEADERSHIP DEVELOPMENT</div>
  </div>
  <div class="svc right" style="left:640px;top:2265px">
    <div class="photo" style="inset:0;background:linear-gradient(135deg,#9aa3ab,#4e5459 55%,#c9c6c0)" role="img" aria-label="Coach speaking with a listener in an office"></div>
    <div class="play" style="left:185px;top:150px"><svg width="34" height="34" viewBox="0 0 24 24"><path d="M7 4l14 8-14 8z" fill="#141414"/></svg></div>
    <div class="label">MOTIVATION</div>
  </div>
  <div class="abs center-badge"><div class="inner">SILVER<br>HARBOR<br>INSTITUTE</div></div>
</section>

<section class="teach">
  <div class="abs edge-top"></div>
  <h2 class="section-title heading">WHAT WE TEACH</h2>
  <div class="tcard" style="left:100px">
    <div class="photo" style="background:linear-gradient(135deg,#8d8f92,#3c3d40 60%,#b8b4ac)" role="img" aria-label="Jujitsu partners drilling a throw on the mat"></div>
    <h3 class="heading">JUJITSU</h3>
    <p>Lorem ipsum dolor sit amet, eiusmod tempor incididunt ut labore et dolore magna aliqua.</p>
  </div>
  <div class="tcard" style="left:445px">
    <div class="photo" style="background:linear-gradient(135deg,#3b6fb0,#c23a3a 55%,#2d3c5a)" role="img" aria-label="Fighters training combatives on blue and red mats"></div>
    <h3 class="heading">COMBATIVE</h3>
    <p>Lorem ipsum dolor sit amet, eiusmod tempor incididunt ut labore et dolore magna aliqua.</p>
  </div>
  <div class="tcard" style="left:790px">
    <div class="photo" style="background:linear-gradient(135deg,#e9e4dc,#c8a98e 55%,#f2efe9)" role="img" aria-label="Meditative coaching session in a bright room"></div>
    <h3 class="heading">METAPHYSICAL</h3>
    <p>Lorem ipsum dolor sit amet, eiusmod tempor incididunt ut labore et dolore magna aliqua.</p>
  </div>
  <div class="abs edge-bottom" style="bottom:-1px"></div>
</section>

<section class="blog">
  <h2 class="section-title heading" style="top:3865px">LATEST BLOG</h2>
  <article class="bcard" style="left:100px;top:3955px;width:480px;height:540px">
    <div class="photo" style="left:0;top:0;width:480px;height:300px;background:linear-gradient(135deg,#6e7d86,#2d3942 55%,#c9c2b4)" role="img" aria-label="Judo athlete mid-throw in a gym"></div>
    <h4 style="left:26px;top:330px;width:430px">Lorem ipsum dolor sit amet, coctetur adipiscing elitsed do eius tempor</h4>
    <div class="date" style="left:26px;top:470px"><svg width="20" height="20" viewBox="0 0 24 24"><rect x="3" y="5" width="18" height="16" rx="2" fill="none" stroke="#5c5c5c" stroke-width="2"/><path d="M3 10h18M8 3v4M16 3v4" stroke="#5c5c5c" stroke-width="2"/></svg>17/09/2022</div>
  </article>
  <article class="bcard" style="left:605px;top:3955px;width:500px;height:265px">
    <div class="photo" style="left:12px;top:12px;width:240px;height:241px;background:linear-gradient(135deg,#e8e6e2,#b9b3aa 55%,#8a2c2c)" role="img" aria-label="Two karate students sparring in white uniforms"></div>
    <h4 style="left:270px;top:22px;width:215px">Lorem ipsum dolor adipiscing el do</h4>
    <p style="left:270px;top:90px;width:215px">Lorem ipsum dolor sit amet, sed do eiusmod tempor incididunt ut labore et dolore magna aliqua. Ut enim ad minim exercitation consequat...</p>
    <div class="date" style="left:270px;top:222px"><svg width="18" height="18" viewBox="0 0 24 24"><rect x="3" y="5" width="18" height="16" rx="2" fill="none" stroke="#5c5c5c" stroke-width="2"/><path d="M3 10h18M8 3v4M16 3v4" stroke="#5c5c5c" stroke-width="2"/></svg>17/09/2022</div>
  </article>
  <article class="bcard" style="left:605px;top:4240px;width:500px;height:265px">
    <div class="photo" style="left:12px;top:12px;width:240px;height:241px;background:linear-gradient(135deg,#4f6fa8,#d9d9df 55%,#2b3550)" role="img" aria-label="Judo players grappling on a blue mat"></div>
    <h4 style="left:270px;top:22px;width:215px">Lorem ipsum dolor adipiscing el do</h4>
    <p style="left:270px;top:90px;width:215px">Lorem ipsum dolor sit amet, sed do eiusmod tempor incididunt ut labore et dolore magna aliqua. Ut enim ad minim exercitation consequat...</p>
    <div class="date" style="left:270px;top:222px"><svg width="18" height="18" viewBox="0 0 24 24"><rect x="3" y="5" width="18" height="16" rx="2" fill="none" stroke="#5c5c5c" stroke-width="2"/><path d="M3 10h18M8 3v4M16 3v4" stroke="#5c5c5c" stroke-width="2"/></svg>17/09/2022</div>
  </article>
</section>

<footer class="footer">
  <div class="abs edge-top"></div>
  <div class="abs f-brand">
    <div class="mark"></div>
    <div class="name">SILVER HARBOR<br>INSTITUTE</div>
  </div>
  <div class="abs f-social"></div>
  <div class="abs f-col" style="left:370px;top:140px">
    <h5>LINKS</h5>
    <ul><li>Home</li><li>Training</li><li>Emotional Intelligence</li><li>Leadership Development</li><li>Motivation</li></ul>
  </div>
  <div class="abs f-col" style="left:590px;top:140px;width:240px">
    <h5>CONTACT US</h5>
    <div class="contact-row"><span class="ic"><svg width="16" height="16" viewBox="0 0 24 24"><path d="M12 2a7 7 0 0 0-7 7c0 5 7 13 7 13s7-8 7-13a7 7 0 0 0-7-7zm0 9.5A2.5 2.5 0 1 1 12 6.5a2.5 2.5 0 0 1 0 5z" fill="#1b1b1c"/></svg></span><span>123 ipsum dolor sit amet, consectetur adipiscing elit</span></div>
    <div class="contact-row"><span class="ic"><svg width="15" height="15" viewBox="0 0 24 24"><path fill="#1b1b1c" d="M6.6 10.8a15 15 0 0 0 6.6 6.6l2.2-2.2c.3-.3.7-.4 1-.2 1.1.4 2.3.6 3.6.6.6 0 1 .4 1 1V20c0 .6-.4 1-1 1A17 17 0 0 1 3 4c0-.6.4-1 1-1h3.5c.6 0 1 .4 1 1 0 1.3.2 2.5.6 3.6.1.3 0 .7-.2 1z"/></svg></span><span style="padding-top:7px">+555 019 4820</span></div>
    <div class="contact-row"><span class="ic"><svg width="16" height="16" viewBox="0 0 24 24"><rect x="3" y="5" width="18" height="14" rx="2" fill="#1b1b1c"/><path d="M3 7l9 6 9-6" stroke="#fff" stroke-width="1.6" fill="none"/></svg></span><span style="padding-top:7px">info@silver-harbor.com</span></div>
  </div>
  <div class="abs f-col" style="left:865px;top:140px">
    <h5>SIGN UP</h5>
    <div class="field">Enter Email here.....</div>
    <div class="submit"><svg width="16" height="16" viewBox="0 0 24 24"><path d="M2 12l20-9-8 20-3-8z" fill="#fff"/></svg>SUBMIT</div>
  </div>
  <div class="abs copy">COPYRIGHT: 2022 SILVER HARBOR INSTITUTE. ALL RIGHTS RESERVED</div>
</footer>

</body>
</html>
```